Annual Meeting/Sci Session/Riddlequest Brochure

We host an educational conference for physicians each year, but this year is our *90th year* so we're going big. We have decided to add break-out sessions (tracks) to our conference, which is usually only one track and held in only one room.

Each year we mail out a brochure, and I have attached last year's as a reference (see "2017 Brochure" attachment). Also attached is a copy of the Save The Date we did earlier this year, so it would be nice if this brochure was similar to that design, but it's not necessary.

I have attached a sample of the type of agenda (table) I am looking for, but we obviously want it to look much nicer than this. The lectures in the GREEN are plenary sessions (all attendees together in the same room), and the lectures in BLUE are break-out sessions (attendees go to separate rooms).

This brochure will be three events rolled into one, with the Scientific Session being the most prominent.

* EVENT NAMES:
"The 90th Annual Harbor Lumen Forum"
"The 28th Annual Assembly"
"The 2nd Annual Quarry Vale TRX Riddlequest Contest"

* SIZE: In the past, we have done a double-gate fold, which is 22.5" wide x 8.5" tall (double-sided art) that the printer folds down to 5.5" x 8.5" (with space for the stamp and address. Your art can be smaller but not larger. It should be able to fold and have space for an address to be printed.

* CONTENT: In addition to the agenda/table, there will need to be a "cover," room for the faculty names and their organizations, room for the Program Description, room for the Target Audience, room for the Program Objectives, room for the boards of directors (3), room for registration rates, room for the Physician Continuing Medical Education section, room for the Disclosure of Conflicts of Interest section, room for the OSB section and QGR section (with logos), room for how-to-register information and room for the Riddlequest event details (and address and cost).

* LOGOS: We will need to have our CHAPTER logo, SOCIETY logo, "90th" logo, Bramwell Pulse Institute logo, and the QGR logo somewhere on the document.

* IMAGERY: I have high-resolution photos of past Annual Meetings and Riddlequest events if needed. It's not crucial that this brochure have pictures though.

* MORE INFO:
Scientific Session event page: http://qv-trx.example/yearlymtg18/
TRX Riddlequest event page: http://qv-trx.example/evening-mixer-and-trx-riddlequest/

Target Market(s)

Brochure will be mailed to our members

Industry/Entity Type

Medicine

Requirements
Must have
• Must have a "table," design or infographic that clearly shows the schedule of events (plenary sessions and break-out sessions). Must have event names, room for faculty names and their organizations, the Program Description, the Target Audience, the Program Objectives, the 3 boards of directors, registration rates, the CME info section, the Disclosure of COI info, the OSB section and QGR section (both with logos), how-to-register information and the Riddlequest event details (with room for the address and cost details).
• * SIZE: In the past, we have done a double-gate fold, which is 22.5" wide x 8.5" tall (double-sided art) that the printer folds down to 5.5" x 8.5" (with space for the stamp and address. Your art can be smaller but not larger. It should be able to fold and have space for an address to be printed.
• * LOGOS: We will need to have our CHAPTER logo, SOCIETY logo, "90th" logo, Bramwell Pulse Institute logo, and the QGR logo somewhere on the document.
Nice to have
• Nice to have a design that looks somewhat similar to the Save The Date that was sent out (attached, "SaveTheDate_sourcefile")
Should not have
• Should not have stock imagery of people or be too cartoonish. These are physicians, many at the very top of their field, and this is their annual, professional educational event. Even though it's our 90th "birthday," this is not a party and should not look too celebratory.

```html
<!DOCTYPE html>
<html lang="en">
<head>
<meta charset="utf-8">
<title>Harbor Lumen Forum Brochure</title>
<link href="https://fonts.googleapis.com/css2?family=Barlow+Semi+Condensed:wght@400;500;600;700&family=Open+Sans:wght@400;600;700&display=swap" rel="stylesheet">
<style>
  :root {
    --navy: #1e3a6c;
    --navy-deep: #172f5a;
    --ink: #1c2b4a;
    --text: #2a3550;
    --rule: #2a3550;
    --highlight: #dde9f6;
    --paper: #ffffff;
    --backdrop: #eef2f4;
  }
  * { box-sizing: border-box; margin: 0; padding: 0; }
  html, body { width: 1200px; height: 695px; overflow: hidden; }
  body { background: var(--backdrop); font-family: "Open Sans", sans-serif; color: var(--text); position: relative; }

  .brochure { position: absolute; left: 30px; top: 127px; width: 1140px; height: 440px; display: flex; box-shadow: 0 2px 10px rgba(20,40,70,.15); }
  .panel { width: 285px; height: 440px; background: var(--paper); position: relative; overflow: hidden; }
  .panel + .panel { border-left: 1px solid #e2e6ec; }

  /* Program table */
  .program-title { position: absolute; left: 14px; top: 50px; font-family: "Barlow Semi Condensed", sans-serif; font-weight: 600; font-size: 21px; color: var(--ink); }
  .schedule { position: absolute; left: 13px; top: 82px; width: 256px; border-collapse: collapse; font-size: 6.4px; line-height: 1.35; color: #222; }
  .schedule td { border: 1px solid var(--rule); text-align: center; vertical-align: middle; padding: 3px; }
  .schedule td.time { width: 40px; text-align: left; padding-left: 4px; }
  .schedule tr.plenary-blue td.session { background: var(--highlight); }
  .schedule .room { font-weight: 700; display: block; margin-top: 2px; }
  .schedule tr.r1 { height: 43px; } .schedule tr.r2 { height: 43px; } .schedule tr.r3 { height: 43px; }
  .schedule tr.r4 { height: 45px; } .schedule tr.r5 { height: 132px; } .schedule tr.r6 { height: 41px; }
  .schedule .room-c { margin-top: 14px; }

  /* Mailing panel */
  .vertical { position: absolute; writing-mode: vertical-rl; transform: rotate(180deg); white-space: nowrap; }
  .return-address { left: 50px; bottom: 82px; font-size: 6.6px; line-height: 1.3; color: var(--ink); }
  .return-seal { position: absolute; left: 46px; top: 382px; width: 36px; height: 36px; border: 1.5px solid var(--ink); border-radius: 50%; }
  .events-block { left: 168px; bottom: 26px; color: var(--ink); display: flex; gap: 4px; }
  .events-url { font-family: "Barlow Semi Condensed", sans-serif; font-weight: 700; font-size: 10px; letter-spacing: .3px; }
  .events-list { font-size: 7px; line-height: 1.25; list-style: none; }
  .events-list li { position: relative; padding-top: 10px; }
  .events-list li::before { content: ""; position: absolute; top: 2px; left: 50%; width: 2.5px; height: 2.5px; background: var(--ink); border-radius: 50%; }

  /* Cover */
  .cover { background: linear-gradient(180deg, var(--navy) 0%, var(--navy-deep) 100%); color: #fff; font-family: "Barlow Semi Condensed", sans-serif; }
  .cover-frame { position: absolute; inset: 9px 9px 12px 12px; border: 1px solid rgba(255,255,255,.9); }
  .heart-art { position: absolute; left: 32px; top: 195px; width: 120px; height: 170px; border-radius: 50% 45% 40% 50%; background: radial-gradient(ellipse at 50% 45%, rgba(120,150,200,.22), rgba(120,150,200,0) 70%); }
  .forum-mark { position: absolute; left: 36px; top: 56px; display: flex; align-items: center; gap: 10px; font-weight: 600; font-size: 27px; line-height: 1.02; color: #fff; }
  .forum-mark .dot { width: 14px; height: 14px; border-radius: 50%; background: #fff; flex: none; }
  .event-stack { position: absolute; right: 24px; top: 198px; width: 150px; text-align: right; }
  .event-stack .lead { font-size: 15px; font-weight: 400; }
  .event-stack .big { font-size: 32px; font-weight: 700; line-height: .95; }
  .event-stack .sub { font-size: 15px; line-height: 1.1; font-weight: 400; }
  .event-stack hr { border: 0; border-top: 1.5px solid #fff; margin: 8px 0 8px 30px; }
  .sponsors { position: absolute; left: 22px; right: 20px; top: 372px; display: flex; flex-wrap: wrap; justify-content: center; row-gap: 7px; column-gap: 6px; font-family: "Open Sans", sans-serif; font-size: 3.8px; line-height: 1.25; }
  .sponsor { display: flex; align-items: center; gap: 3px; width: 76px; min-width: 0; }
  .sponsor .seal { width: 16px; height: 16px; border: 1px solid #fff; border-radius: 50%; flex: none; }
  .sponsor .caption { flex: 1; min-width: 0; white-space: nowrap; }

  /* Description panel */
  .info { padding: 44px 14px 0 14px; font-size: 5.6px; line-height: 1.3; color: var(--text); }
  .info h2 { font-family: "Open Sans", sans-serif; font-weight: 700; font-size: 7.4px; color: var(--ink); margin-bottom: 2px; letter-spacing: .1px; }
  .info p { margin-bottom: 4px; }
  .info section { margin-bottom: 12px; }
  .objectives { list-style: none; }
  .objectives li { position: relative; padding-left: 6px; margin-bottom: 5px; }
  .objectives li::before { content: "•"; position: absolute; left: 0; }
  .thanks { font-style: italic; text-align: center; font-size: 5px; margin-top: 10px; }
</style>
</head>
<body>
<div class="brochure">

  <div class="panel program-panel">
    <h1 class="program-title">Program Table</h1>
    <table class="schedule">
      <tr class="r1 plenary-blue"><td class="time">9 a.m.</td><td class="session" colspan="3">Registration<span class="room">Auditorium</span></td></tr>
      <tr class="r2"><td class="time">9:30 a.m.</td><td class="session" colspan="3">Welcome<span class="room">Auditorium</span></td></tr>
      <tr class="r3 plenary-blue"><td class="time">9:45 a.m.</td><td class="session" colspan="3">“PSCK9 Inhibitors in Dyslipidemia” – Helena Marsh, MD, MPH<span class="room">Auditorium</span></td></tr>
      <tr class="r4"><td class="time">10:45 a.m.</td><td class="session" colspan="3">“Title Forthcoming” – Victor L. Amrein, MD, MBA, FCHM<span class="room">Auditorium</span></td></tr>
      <tr class="r5"><td class="time">11:30 a.m.</td>
        <td class="session">“MIPS or MOOPS? Lessons Learned from Year 1 of the Quality Payment Program and What’s in Store for the Future” – Dana Okafor<span class="room room-c">Room C198</span></td>
        <td class="session">“Negotiating Contracts” – [Speaker TBD]<span class="room room-c">Room 9204</span></td>
        <td class="session">“Journal Club: Summary of the Top Trials of 2018” [Speakers TBD]<span class="room room-c">Room 9205</span></td></tr>
      <tr class="r6"><td class="time">12:30 p.m.</td><td class="session" colspan="3">Lunch ‘n’ Learn - 12:30 p.m.<span class="room">Rooms C201, C202, C203, C204 &amp; C205</span></td></tr>
    </table>
  </div>

  <div class="panel mailing-panel">
    <div class="vertical return-address">The Quarry Vale Cardiac Society, Inc.<br>210 Lindell Row, Suite 400<br>Quarry Vale, QV 20410</div>
    <div class="return-seal"></div>
    <div class="vertical events-block">
      <div class="events-url">QV-TRX.EXAMPLE/EVENTS</div>
      <ul class="events-list">
        <li>The 89th Annual Harbor Lumen Forum of the<br>Quarry Vale Cardiac Society, Inc.</li>
        <li>The 27th Annual Assembly of the<br>Quarry Vale State Chapter of the<br>Collegium of Heart Medicine</li>
      </ul>
    </div>
  </div>

  <div class="panel cover">
    <div class="cover-frame"></div>
    <div class="heart-art" role="img" aria-label="Faint anatomical heart illustration"></div>
    <div class="forum-mark"><span class="dot"></span><span>The 90th<br>Annual Harbor<br>Lumen Forum</span></div>
    <div class="event-stack">
      <div><span class="lead">The</span><span class="big">28th</span></div>
      <div class="sub">Annual Assembly</div>
      <hr>
      <div><span class="lead">The</span><span class="big">2nd</span></div>
      <div class="sub">Annual Quarry Vale<br>TRX Riddlequest<br>Contest</div>
    </div>
    <div class="sponsors">
      <div class="sponsor"><span class="seal"></span><span class="caption">Presented by<br>The Quarry Vale<br>Cardiac Society Inc.</span></div>
      <div class="sponsor"><span class="seal"></span><span class="caption">of the<br>Quarry Vale State Chapter,<br>Collegium of Heart<br>Medicine</span></div>
      <div class="sponsor"><span class="seal"></span><span class="caption">in association with<br>Bramwell Pulse<br>Institute</span></div>
      <div class="sponsor"><span class="seal"></span><span class="caption">Fostering the<br>Quarry Vale/Meridia<br>Chapter Exchange<br>Program</span></div>
      <div class="sponsor"><span class="seal"></span><span class="caption">Jointly provided by<br>QGR · Institute for<br>Graduate Review</span></div>
    </div>
  </div>

  <div class="panel">
    <div class="info">
      <section>
        <h2>PROGRAM DESCRIPTION</h2>
        <p>This annual event brings together cardiologists, cardio-thoracic surgeons, internists, family practitioners, gerontologists, oncologists, cardiac nurse practitioners, physician assistants, cardiology fellows in training (FITs) and all members of the cardiovascular team. The event is presented by the Quarry Vale Cardiac Society, the Quarry Vale State Chapter of the Collegium of Heart Medicine and the Bramwell Pulse Institute.</p>
        <p>This year’s conference will feature the winners of the Annual Young Investigators’ Competition, which is now open, and this year will ALSO feature the winners of the inaugural QV TRX Riddlequest Contest!</p>
      </section>
      <section>
        <h2>TARGET AUDIENCE</h2>
        <p>This activity is intended for cardiologists, cardiothoracic surgeons, internists, family medicine practitioners, gerontologists, oncologists, cardiac nurse practitioners, physician assistants, cardiology fellows-in-training (FITs), all members of the cardiovascular team and any other healthcare professionals engaged in the care of patients with CVD.</p>
      </section>
      <section>
        <h2>PROGRAM OBJECTIVES</h2>
        <p>After completing this activity, the participant should be better able to:</p>
        <ul class="objectives">
          <li>Explain differences and similarities in AMI presentation and management between Quarry Vale and Meridia, analyze the reasons for these differences and identify the barriers to perform rapid reperfusion therapy</li>
          <li>Explain the importance of ICMP in the epidemiology and mortality attributed to heart failure and describe the treatment modalities available to improve the prognosis of patients with ICMP</li>
          <li>Discuss the value of different test results in selecting patients with ICMP with greatest potential for benefit from surgical revascularization</li>
          <li>Describe potential advantages of a robotic totally endoscopic procedure</li>
          <li>Identify candidates for robotic totally endoscopic mitral valve repair</li>
          <li>Determine when it is proper to use new oral anticoagulants in ACS</li>
          <li>Determine current biomarkers and their role in establishing the diagnosis and prognosis of heart failure</li>
          <li>Differentiate between the type and severity of heart failure based on patient history, evaluation and diagnostic workup</li>
          <li>Describe the benefits and limitations of current heart failure therapies and discuss new and emerging therapies for heart failure and their role in the therapeutic management</li>
          <li>Explain the effects and implications of risk factors and comorbidities on potassium levels and hyperkalemia in heart failure patients</li>
        </ul>
        <p class="thanks">The Quarry Vale Cardiac Society and Quarry Vale State Chapter of the Collegium of Heart Medicine<br>thank Bramwell Pulse Institute for its continuing educational support.</p>
      </section>
    </div>
  </div>

</div>
</body>
</html>
```